Event Production Company needs a Poster for a karaoke party

We need a poster similar to the one attached (the same typology of the logo), in which it can be seen that there are three prizes for the winners, a presenter and a jury. The room where the party is held is in Verul next Saturday, December 17, 2022. We are looking for an innovative poster, with a youthful air and a desire to party
Target Market(s)
Young people between 16 and 20 years old
Other font styles liked:
- Pump Triline

Colors
E54698
E96AAD
F1A4CE
F9D9EA
FCEFF6
A7469A
B969AE
D3A5CF
EDDBEB
F8F0F9
6B429C
8869AF
B7A5CE
E3DAEB
F3F0F8
Requirements
Must have
- Fluorescent colors (neon), date, time and day of the event, the instagram profile has to appear

Nice to have
- that the gifts that are offered appear

Should not have
- little relevant information

```html
<!DOCTYPE html>
<html lang="es">
<head>
<meta charset="utf-8">
<title>Vibe Karaoke — Verul</title>
<link rel="stylesheet" href="https://fonts.googleapis.com/css2?family=Montserrat:wght@500;600;700&display=swap">
<style>
  :root {
    --stage: #d5d7d6;
    --ink: #111116;
    --neon-pink: #e54698;
    --pink-soft: #f1a4ce;
    --pink-pale: #f9d9ea;
    --white: #ffffff;
    --gift-red: #e8284f;
  }
  * { margin: 0; padding: 0; box-sizing: border-box; }
  html, body { width: 1200px; height: 2294px; overflow: hidden; background: var(--stage); }
  .poster {
    position: absolute; left: 30px; top: 341px;
    width: 1140px; height: 1611px;
    background: var(--ink); overflow: hidden;
    font-family: "Montserrat", sans-serif; color: var(--white);
    box-shadow: 0 12px 30px rgba(0,0,0,.35);
  }
  .hero-photo {
    position: absolute; left: 0; top: 0; width: 100%; height: 900px;
    background:
      radial-gradient(ellipse 420px 300px at 560px 150px, rgba(255,220,230,.85), rgba(255,90,120,0) 70%),
      linear-gradient(180deg, #ff3a55 0%, #f03a6c 35%, #b0244f 58%, #3a1020 80%, var(--ink) 100%);
  }
  .venue {
    position: absolute; left: 72px; top: 80px;
    font-weight: 700; font-size: 62px; letter-spacing: 10px; color: var(--white);
  }
  .event-name { font-weight: 700; color: var(--white); }
  .event-name__line {
    position: absolute; left: 62px;
    font-size: 230px; line-height: 1; letter-spacing: -4px; white-space: nowrap;
  }
  .event-name__line--top { top: 140px; }
  .event-name__line--bottom { top: 330px; }
  .date-band {
    position: absolute; left: 69px; top: 588px; width: 959px; height: 92px;
    background: var(--neon-pink);
    display: flex; align-items: center; justify-content: center;
    font-weight: 700; font-size: 47px;
  }
  .features {
    position: absolute; left: 72px; top: 735px; list-style: none;
    font-weight: 600; font-size: 40px; line-height: 66px;
  }
  .features li { display: flex; align-items: center; }
  .features li::before {
    content: ""; width: 26px; height: 26px; border-radius: 50%;
    border: 5px solid var(--pink-soft); background: var(--neon-pink);
    margin-right: 32px; flex: none;
  }
  .gift {
    position: absolute; border-radius: 6px;
    background: linear-gradient(180deg, #c81b3f 0%, var(--gift-red) 30%, #b81a3a 100%);
  }
  .gift--first { left: 74px; top: 1036px; width: 292px; height: 345px; }
  .gift--second { left: 412px; top: 1100px; width: 241px; height: 281px; }
  .gift--third { left: 696px; top: 1158px; width: 197px; height: 223px; }
  .rank {
    position: absolute; border-radius: 50%; background: var(--white); color: var(--ink);
    display: flex; align-items: center; justify-content: center; font-weight: 600;
  }
  .rank--first { left: 275px; top: 1292px; width: 104px; height: 104px; font-size: 44px; }
  .rank--second { left: 588px; top: 1304px; width: 90px; height: 90px; font-size: 44px; }
  .rank--third { left: 847px; top: 1323px; width: 74px; height: 74px; font-size: 40px; }
  .prize {
    position: absolute; top: 1402px; width: 200px; margin-left: -100px; text-align: center;
    font-weight: 700; font-size: 42px; color: var(--pink-soft);
  }
  .info-bar {
    position: absolute; left: 83px; top: 1472px; width: 818px; height: 69px;
    border: 2px solid var(--white); border-radius: 14px; overflow: hidden; display: flex;
  }
  .info-bar__label {
    width: 409px; display: flex; align-items: center; justify-content: center;
    font-weight: 500; font-size: 31px;
  }
  .info-bar__handle {
    flex: 1; background: var(--white); color: var(--neon-pink);
    display: flex; align-items: center; justify-content: center;
    font-weight: 500; font-size: 33px;
  }
</style>
</head>
<body>
  <main class="poster">
    <div class="hero-photo" role="img" aria-label="Concierto con focos rojos y rosas sobre el público"></div>
    <div class="venue">VERUL</div>
    <h1 class="event-name">
      <span class="event-name__line event-name__line--top">vibe</span>
      <span class="event-name__line event-name__line--bottom">karaoke</span>
    </h1>
    <div class="date-band">sábado, 17 de diciembre de 2022</div>
    <ul class="features">
      <li>PRESENTADO POR:</li>
      <li>LARA MONTES Y NURIA VIDAL</li>
      <li>JURADO PROFESIONAL</li>
      <li>+ 1000€ EN PREMIOS</li>
    </ul>
    <div class="gift gift--first" role="img" aria-label="Caja de regalo roja con lazo, primer premio"></div>
    <div class="gift gift--second" role="img" aria-label="Caja de regalo roja con lazo, segundo premio"></div>
    <div class="gift gift--third" role="img" aria-label="Caja de regalo roja con lazo, tercer premio"></div>
    <div class="rank rank--first">1</div>
    <div class="rank rank--second">2</div>
    <div class="rank rank--third">3</div>
    <div class="prize" style="left:216px">500€</div>
    <div class="prize" style="left:529px">300€</div>
    <div class="prize" style="left:793px">150€</div>
    <div class="info-bar">
      <div class="info-bar__label">TODA LA INFO :</div>
      <div class="info-bar__handle">@VIBEKARAOKE</div>
    </div>
  </main>
</body>
</html>
```